Powerpoint presentation about personal finance

Investing 4$ per day is what has been required to become a millionaire by investing in the stock market from 1965 to 2015. Yet only 1% of the population is millionaire. This presentation is about the most common causes why people do not build significant wealth through their life. We intend to educate people with this presentation, but also build trust so they become client of our wealth management firm. Feel free to send us any question about this project.
Updates

Reason: I have uploaded the logo source file and an updated PPT file. Thanks

Target Market(s)

People with a willingness to save money between the age of 20 to 50 years old

Industry/Entity Type

Finance

Font styles to use
Sans Serif

Requirements
Must have
• We are looking at uniforming the design throughout the presentation with nice, classic tone colors, large font size as it needs to be visible 3 meters apart. The content of the presentation will be updated regularly.
Should not have
• cartoon style, not serious

```html
<!DOCTYPE html>
<html lang="fr">
<head>
<meta charset="utf-8">
<title>Norval – présentation finances personnelles</title>
<link rel="stylesheet" href="https://fonts.googleapis.com/css2?family=Fira+Sans:wght@300;400;600&family=Merriweather:wght@400;700;900&display=swap">
<style>
  :root{
    --page:#cfcfcf;
    --slide:#ffffff;
    --ink:#1f1f1f;
    --ink-soft:#3a3a3a;
    --blue:#1a48a0;
    --green:#3c9a35;
    --grid:#e6e6e6;
  }
  *{box-sizing:border-box;margin:0;padding:0}
  html,body{width:1200px;height:1200px;overflow:hidden;background:var(--page)}
  .deck{position:relative;width:1200px;height:1200px}
  .slide{position:absolute;width:563px;height:317px;background:var(--slide);overflow:hidden;
    box-shadow:1px 2px 4px rgba(0,0,0,.35);font-family:"Fira Sans",sans-serif;color:var(--ink)}
  .col-a{left:21px}.col-b{left:610px}
  .row-1{top:53px}.row-2{top:442px}.row-3{top:830px}

  .foliage{position:absolute;pointer-events:none}
  .foliage--right{right:-40px;bottom:-60px;width:330px;height:260px;
    background:radial-gradient(ellipse at 60% 60%,rgba(200,200,200,.55),rgba(225,225,225,.25) 55%,rgba(255,255,255,0) 75%)}
  .foliage--left{left:-30px;top:-20px;width:330px;height:360px;
    background:radial-gradient(ellipse at 40% 45%,rgba(205,205,205,.6),rgba(225,225,225,.3) 55%,rgba(255,255,255,0) 78%)}

  .rule{position:absolute;height:2.5px}
  .rule--blue{background:var(--blue)}
  .rule--green{background:var(--green)}

  .brand-mark{position:absolute;display:flex;align-items:center;justify-content:center;
    width:46px;height:46px;border-radius:50%;border:3px solid var(--blue);
    font-family:"Fira Sans",sans-serif;font-weight:600;font-size:10px;color:var(--blue)}
  .brand-mark--corner{top:19px;right:22px}

  .brand-lockup{position:absolute;left:355px;top:38px;display:flex;align-items:center;gap:6px}
  .brand-lockup .brand-dot{width:42px;height:42px;border-radius:50%;border:3px solid var(--blue)}
  .brand-lockup .brand-name{font-weight:600;font-size:21px;color:var(--blue);line-height:1}
  .brand-lockup .brand-tag{font-weight:600;font-size:6.5px;letter-spacing:1.5px;color:var(--blue);text-transform:uppercase;line-height:1.3;margin-top:2px}

  .cover-title{position:absolute;left:32px;top:194px;font-family:"Merriweather",serif;font-weight:900;font-size:30px;letter-spacing:2.2px}
  .cover-sub{position:absolute;left:32px;top:240px;font-family:"Merriweather",serif;font-size:15px;color:var(--ink-soft)}

  .heading{position:absolute;left:32px;top:28px;font-family:"Merriweather",serif;font-weight:700;font-size:28px;color:#333}
  .lead{position:absolute;left:0;width:100%;top:93px;text-align:center;font-weight:600;font-size:18.5px;color:var(--blue)}
  .body{position:absolute;left:20px;right:20px;top:140px;text-align:center;font-size:19px;line-height:25.6px;font-weight:400;white-space:nowrap}

  .statement{position:absolute;left:20px;right:20px;top:70px;text-align:center;font-size:19px;line-height:38px;font-weight:400;white-space:nowrap}
  .statement em{font-style:normal;font-weight:600;color:var(--blue)}

  .question{position:absolute;left:10px;right:10px;top:68px;text-align:center;font-family:"Merriweather",serif;font-weight:400;font-size:20.5px;line-height:44px;white-space:nowrap}
  .question strong{color:var(--blue);font-weight:700}

  .list-title{position:absolute;left:32px;top:26px;width:440px;font-family:"Merriweather",serif;font-weight:700;font-size:15px;line-height:20px;color:#333}
  .factor-list{position:absolute;left:45px;top:88px;width:468px;list-style:none;font-size:14.5px;line-height:19.5px;font-weight:400}
  .factor-list li{position:relative;padding-left:25px;margin-bottom:2px;text-align:justify}
  .factor-list li::before{content:"";position:absolute;left:2px;top:7px;width:5px;height:5px;background:var(--blue)}
  .justify-line{display:block;text-align:justify;text-align-last:justify}

  .chart-title{position:absolute;left:32px;top:4px;font-family:"Merriweather",serif;font-weight:700;font-size:14.5px;line-height:20px;color:#333;white-space:nowrap}
  .chart{position:absolute;left:0;top:0}
  .chart text{font-family:"Fira Sans",sans-serif;font-size:11px;fill:#333}
</style>
</head>
<body>
<main class="deck">

  <section class="slide col-a row-1 slide--cover">
    <div class="foliage foliage--left" role="img" aria-label="Feuillage décoratif gris pâle"></div>
    <div class="brand-lockup">
      <span class="brand-dot"></span>
      <div>
        <div class="brand-name">NORVAL</div>
        <div class="brand-tag">Financial planning<br>&amp; wealth management</div>
      </div>
    </div>
    <h1 class="cover-title">Title text</h1>
    <p class="cover-sub">Subtitle</p>
    <span class="rule rule--blue" style="left:32px;top:270px;width:266px"></span>
    <span class="rule rule--green" style="left:54px;top:274px;width:266px"></span>
  </section>

  <section class="slide col-b row-1">
    <div class="foliage foliage--right" role="img" aria-label="Feuillage décoratif gris pâle"></div>
    <span class="brand-mark brand-mark--corner">Norval</span>
    <h2 class="heading">L’inaction…</h2>
    <span class="rule rule--blue" style="left:28px;top:68px;width:249px"></span>
    <span class="rule rule--green" style="left:50px;top:72px;width:249px"></span>
    <p class="lead">Vous croyez ne pas avoir les moyens d’épargner?</p>
    <p class="body">Pour générer 4$ par jour,<br>il ne suffit que de se faire son café et son muffin à<br>la maison le matin au lieu de l’acheter sur la route!<br>On ne parle pas ici d’un grand sacrifice pour<br>pouvoir espéré réaliser nos rêves!</p>
  </section>

  <section class="slide col-a row-2">
    <div class="foliage foliage--right" role="img" aria-label="Feuillage décoratif gris pâle"></div>
    <span class="brand-mark brand-mark--corner">Norval</span>
    <p class="statement">Malheureusement, peu de gens arrivent à obtenir<br><em>l’indépendance financière</em> qui leur procurerait un<br>tel niveau de sécurité et de liberté, pourtant ce<br>rêve a été à la portée de presque tous…</p>
    <span class="rule rule--blue" style="left:56px;top:256px;width:452px"></span>
    <span class="rule rule--green" style="left:80px;top:261px;width:404px"></span>
  </section>

  <section class="slide col-b row-2">
    <div class="foliage foliage--right" role="img" aria-label="Feuillage décoratif gris pâle"></div>
    <span class="brand-mark brand-mark--corner">Norval</span>
    <p class="question"><strong>L’idéal</strong> pour beaucoup d’entre nous n’est-il<br>pas d’avoir suffisamment <strong>d’argent</strong> et<br>d’être en santé afin de pouvoir réaliser nos<br><strong>rêves</strong>?</p>
    <span class="rule rule--blue" style="left:56px;top:256px;width:452px"></span>
    <span class="rule rule--green" style="left:80px;top:261px;width:404px"></span>
  </section>

  <section class="slide col-a row-3">
    <div class="foliage foliage--right" role="img" aria-label="Feuillage décoratif gris pâle"></div>
    <span class="brand-mark brand-mark--corner">Norval</span>
    <h3 class="list-title">Les principaux facteurs qui nuisent à l’atteinte de l’indépendance financière:</h3>
    <span class="rule rule--blue" style="left:28px;top:69px;width:249px"></span>
    <span class="rule rule--green" style="left:50px;top:73px;width:249px"></span>
    <ul class="factor-list">
      <li>L’inaction et le report à plus tard</li>
      <li>Les erreurs émotives (la peur)</li>
      <li><span class="justify-line">Favoriser les plaisirs à court terme plutôt que les bénéfices à</span>long terme</li>
      <li>Le manque de connaissances</li>
      <li>L’accès à l’information</li>
      <li><span class="justify-line">Les frais de gestion et la rémunération des conseiller</span>financiers</li>
      <li>Les impôts</li>
      <li>L’inflation</li>
    </ul>
  </section>

  <section class="slide col-b row-3">
    <span class="brand-mark brand-mark--corner">Norval</span>
    <h3 class="chart-title">Investissement fixe équivalent à 4$ par jour dans le<br>Meridia 500 pour un individu né en 1950 et qui a<br>commencé à épargner à 15 ans</h3>
    <span class="rule rule--blue" style="left:28px;top:68px;width:249px"></span>
    <span class="rule rule--green" style="left:50px;top:72px;width:249px"></span>
    <svg class="chart" width="563" height="317" viewBox="0 0 563 317" role="img" aria-label="Croissance de l’investissement de 1965 à 2015, jusqu’à 1,1 million">
      <text x="32" y="97">$ million</text>
      <g stroke="var(--grid)" stroke-width="1">
        <line x1="55" y1="114.5" x2="543" y2="114.5"/>
        <line x1="55" y1="139" x2="543" y2="139"/>
        <line x1="55" y1="163.5" x2="543" y2="163.5"/>
        <line x1="55" y1="188" x2="543" y2="188"/>
        <line x1="55" y1="212.5" x2="543" y2="212.5"/>
        <line x1="55" y1="237" x2="543" y2="237"/>
        <line x1="55" y1="261.5" x2="543" y2="261.5" stroke="#bdbdbd"/>
      </g>
      <g text-anchor="end">
        <text x="46" y="118">1,2</text>
        <text x="46" y="143">1,0</text>
        <text x="46" y="167">0,8</text>
        <text x="46" y="192">0,6</text>
        <text x="46" y="216">0,4</text>
        <text x="46" y="241">0,2</text>
        <text x="46" y="265">0,0</text>
      </g>
      <polyline fill="none" stroke="var(--blue)" stroke-width="2.2" stroke-linejoin="round"
        points="61,261 108.7,259.8 156.4,258.6 204.1,256.1 251.8,251.2 270.9,248.8 290,241.4 299.5,242.6 309,236.5 328.2,232.8 337.7,232.8 347.2,221.8 356.7,212 366.3,193.6 375.8,177.7 385.3,163 394.9,172.8 404.4,187.5 414,204.6 423.5,190 433,182.6 442.6,180.2 452.1,169.1 461.7,165.5 471.2,203.4 480.7,188.7 490.3,178.9 499.8,177.7 509.3,166.7 518.9,138.5 528.4,123.8 538,123.8"/>
      <g text-anchor="end" font-size="10.5">
        <text transform="translate(65 268) rotate(-90)">1965</text>
        <text transform="translate(84 268) rotate(-90)">1967</text>
        <text transform="translate(103 268) rotate(-90)">1969</text>
        <text transform="translate(122 268) rotate(-90)">1971</text>
        <text transform="translate(141 268) rotate(-90)">1973</text>
        <text transform="translate(160 268) rotate(-90)">1975</text>
        <text transform="translate(179 268) rotate(-90)">1977</text>
        <text transform="translate(198 268) rotate(-90)">1979</text>
        <text transform="translate(218 268) rotate(-90)">1981</text>
        <text transform="translate(237 268) rotate(-90)">1983</text>
        <text transform="translate(256 268) rotate(-90)">1985</text>
        <text transform="translate(275 268) rotate(-90)">1987</text>
        <text transform="translate(294 268) rotate(-90)">1989</text>
        <text transform="translate(313 268) rotate(-90)">1991</text>
        <text transform="translate(332 268) rotate(-90)">1993</text>
        <text transform="translate(351 268) rotate(-90)">1995</text>
        <text transform="translate(370 268) rotate(-90)">1997</text>
        <text transform="translate(389 268) rotate(-90)">1999</text>
        <text transform="translate(408 268) rotate(-90)">2001</text>
        <text transform="translate(427 268) rotate(-90)">2003</text>
        <text transform="translate(447 268) rotate(-90)">2005</text>
        <text transform="translate(466 268) rotate(-90)">2007</text>
        <text transform="translate(485 268) rotate(-90)">2009</text>
        <text transform="translate(504 268) rotate(-90)">2011</text>
        <text transform="translate(523 268) rotate(-90)">2013</text>
        <text transform="translate(542 268) rotate(-90)">2015</text>
      </g>
    </svg>
  </section>

</main>
</body>
</html>
```